Dynamic Business Card for Sports Supplements Company

Hi! I'm looking for an awesome business card to match my existing sports supplement company. I have uploaded my current company logo and screenshot of the front page of my website.

I would like to have something dynamic and interesting and utilize the colors in the website - the reds and purples

The business card should be double sided and focus on a unique eye-catching design on the back and include all the relevant company info.

Most importantly, it should say somewhere: "Sign up on our website for a coupon code."

Target Market(s)

Mostly for women gym goers but it shouldn't be too feminine. It should be in keeping with the website design. It should flow and clearly be connected to it

Industry/Entity Type

Business

Contact Information for Business Card

Lorena K. Vasquez
CEO
LVasquez@Fortivanco.example
www.fortivanco.example
614.275.3081
P.O. Box 48317
Burke, Virginia 22417

Sign up on our website for a coupon code

Font styles to use
Serif
Sans Serif
Other font styles liked:
• Novecento font family and "Fortivan" is in AR Destine font

Requirements
Must have
• One side should be a bold Fortivan logo design. Even just the symbol itself may be o.k. (see attached file)

```html
<!DOCTYPE html>
<html lang="en">
<head>
<meta charset="utf-8">
<title>Fortivan Business Card</title>
<link href="https://fonts.googleapis.com/css2?family=Work+Sans:wght@400;600;700&family=Oswald:wght@500&display=swap" rel="stylesheet">
<style>
  :root {
    --stage: #2a2a2a;
    --card-dark: #141414;
    --card-light: #ffffff;
    --brand-red: #e3262b;
    --ink: #4a4a4a;
    --ink-strong: #3c3c3c;
    --paper-text: #ffffff;
  }
  html, body {
    margin: 0;
    width: 1200px;
    height: 900px;
    overflow: hidden;
    background: var(--stage);
    font-family: "Work Sans", Arial, sans-serif;
  }
  .canvas {
    position: relative;
    width: 1200px;
    height: 900px;
  }
  .card {
    position: absolute;
    left: 250px;
    width: 700px;
    height: 400px;
    border-radius: 22px;
    overflow: hidden;
    box-sizing: border-box;
  }
  /* Back side */
  .card-back {
    top: 40px;
    background: var(--card-dark);
    color: var(--paper-text);
  }
  .back-brand {
    position: absolute;
    left: 0;
    right: 70px;
    top: 150px;
    text-align: center;
  }
  .back-brand .brand-row {
    display: inline-flex;
    align-items: center;
    gap: 16px;
  }
  .brand-square {
    width: 34px;
    height: 34px;
    background: var(--brand-red);
  }
  .back-brand .brand-name {
    font-weight: 700;
    font-size: 52px;
    letter-spacing: 3px;
    text-transform: uppercase;
    line-height: 1;
  }
  .back-brand .tagline {
    margin-top: 10px;
    font-size: 19px;
    letter-spacing: 2.5px;
  }
  .coupon-note {
    position: absolute;
    right: 28px;
    top: 50%;
    transform: translateY(-50%) rotate(90deg);
    transform-origin: center;
    width: 360px;
    margin-right: -165px;
    text-align: center;
    font-family: "Oswald", "Arial Narrow", sans-serif;
    font-weight: 500;
    font-size: 17px;
    letter-spacing: 1px;
    text-transform: uppercase;
    white-space: nowrap;
  }
  /* Front side */
  .card-front {
    top: 470px;
    background: var(--card-light);
  }
  .front-brand {
    position: absolute;
    left: 50px;
    top: 0;
    width: 250px;
    height: 400px;
    display: flex;
    align-items: center;
    justify-content: center;
    gap: 12px;
  }
  .front-brand .brand-name {
    font-weight: 700;
    font-size: 40px;
    letter-spacing: 1px;
    color: var(--brand-red);
    text-transform: uppercase;
  }
  .front-brand .brand-square {
    width: 26px;
    height: 26px;
  }
  .divider {
    position: absolute;
    left: 318px;
    top: 105px;
    width: 2px;
    height: 190px;
    background: var(--brand-red);
  }
  .contact {
    position: absolute;
    left: 350px;
    top: 108px;
    color: var(--ink);
  }
  .contact .person {
    margin: 0;
    font-weight: 700;
    font-size: 25px;
    letter-spacing: 1.5px;
    text-transform: uppercase;
    color: var(--ink-strong);
    line-height: 1.05;
  }
  .contact .person .surname { color: var(--brand-red); }
  .contact .role {
    margin: 0 0 14px;
    font-weight: 700;
    font-size: 17px;
    letter-spacing: 1px;
    color: var(--ink-strong);
  }
  .contact .address {
    margin: 0 0 14px;
    font-size: 18px;
    line-height: 1.2;
    font-style: normal;
  }
  .contact ul {
    list-style: none;
    margin: 0;
    padding: 0;
  }
  .contact li {
    display: flex;
    align-items: center;
    gap: 12px;
    font-size: 18px;
    line-height: 1.45;
  }
  .contact li svg { width: 18px; height: 18px; flex: none; }
  .contact .web-domain { color: var(--brand-red); }
</style>
</head>
<body>
<main class="canvas">
  <section class="card card-back" aria-label="Card back">
    <div class="back-brand">
      <div class="brand-row">
        <span class="brand-square"></span>
        <span class="brand-name">Fortivan</span>
      </div>
      <div class="tagline">Your Performance Partner</div>
    </div>
    <p class="coupon-note">Sign up on our website for a coupon code</p>
  </section>

  <section class="card card-front" aria-label="Card front">
    <div class="front-brand">
      <span class="brand-square"></span>
      <span class="brand-name">Fortivan</span>
    </div>
    <div class="divider"></div>
    <div class="contact">
      <h1 class="person">Lorena <span class="surname">K. Vasquez</span></h1>
      <p class="role">CEO</p>
      <address class="address">P.O. Box 48317 Burke,<br>Virginia 22417</address>
      <ul>
        <li>
          <svg viewBox="0 0 20 20" aria-hidden="true"><path fill="#e3262b" d="M4 2l3 0 1.5 4-2 1.5c1 2.2 2.8 4 5 5l1.5-2 4 1.5 0 3c0 1-1 2-2 2C8 17 3 12 2 4c0-1 1-2 2-2z"/></svg>
          <span>614.275.3081</span>
        </li>
        <li>
          <svg viewBox="0 0 20 20" aria-hidden="true"><rect x="1" y="4" width="18" height="12" fill="#e3262b"/><path d="M1 4l9 7 9-7" fill="none" stroke="#fff" stroke-width="1.6"/></svg>
          <span>LVasquez@Fortivanco.example</span>
        </li>
        <li>
          <svg viewBox="0 0 20 20" aria-hidden="true"><circle cx="12" cy="8" r="5.5" fill="none" stroke="#e3262b" stroke-width="2.2"/><path d="M8 12l-6 6" stroke="#e3262b" stroke-width="2.8" stroke-linecap="round"/></svg>
          <span>www.<span class="web-domain">fortivanco</span>.example</span>
        </li>
      </ul>
    </div>
  </section>
</main>
</body>
</html>
```